Brookfarrow Osteopathy and dry needling business card

Business card for Brookfarrow Osteopathy and Dry Needling.

Industry/Entity Type

Health

Contact Information for Business Card

I do not have a phone number yet. I also do not have an email address yet. The physical address is: 48 Lower Crane Street Brookfarrow The website is: www.brookfarrowosteosteopathy.example My details are: Dr Martin Pellowe, Osteopath (B.Clin.Sci (Ost) M.Ost BSC ECON (Hons)

Colors
0094D4
00A9DD
6FCCEA
C7EBF8
E9F6FB

Requirements
Must have
• logo on the back
Nice to have
• Maybe a space for me to write an appointment time and date on the card.

```html
<!DOCTYPE html>
<html lang="en">
<head>
<meta charset="utf-8">
<title>Brookfarrow Osteopathy and Dry Needling – Business Card</title>
<link rel="stylesheet" href="https://fonts.googleapis.com/css2?family=Montserrat:wght@400;500;700&display=swap">
<style>
  :root {
    --brand-blue: #0F98D4;
    --brand-blue-deep: #0094D4;
    --sun-orange: #F39A2B;
    --card-white: #FFFFFF;
    --ink: #1E1E1E;
    --stage: #3A3A3A;
  }
  * { box-sizing: border-box; margin: 0; padding: 0; }
  html, body { width: 1200px; height: 875px; overflow: hidden; }
  body {
    background: var(--stage);
    font-family: "Montserrat", sans-serif;
    display: flex;
    align-items: center;
    justify-content: center;
    gap: 40px;
  }
  .card {
    position: relative;
    width: 550px;
    height: 314px;
    border-radius: 22px;
    overflow: hidden;
  }

  /* Back side */
  .card-back { background: var(--brand-blue); color: var(--card-white); }
  .back-mark {
    position: absolute;
    left: 50%; top: 30px;
    transform: translateX(-50%);
    width: 190px; height: 190px;
    border: 3px solid var(--card-white);
    border-radius: 50%;
    display: flex; align-items: center; justify-content: center;
    text-align: center;
    padding: 20px;
  }
  .mark-name {
    font-weight: 500;
    font-size: 16px;
    line-height: 1.3;
    letter-spacing: 0.04em;
    text-transform: uppercase;
  }
  .appointment {
    position: absolute;
    left: 34px; right: 34px; bottom: 34px;
    display: flex; gap: 16px;
    font-size: 14px; font-weight: 400;
  }
  .appointment-field { display: flex; align-items: flex-end; flex: 1; gap: 6px; }
  .appointment-field span { white-space: nowrap; }
  .appointment-field i {
    flex: 1;
    border-bottom: 2px dotted var(--card-white);
    margin-bottom: 4px;
  }

  /* Front side */
  .card-front { background: var(--card-white); color: var(--ink); }
  .front-mark {
    position: absolute;
    left: 34px; top: 54px;
    width: 150px; height: 150px;
    border: 3px solid var(--brand-blue);
    border-radius: 50%;
    display: flex; align-items: center; justify-content: center;
    text-align: center;
    padding: 14px;
    color: var(--brand-blue);
  }
  .front-mark .mark-name { font-size: 12px; }
  .divider {
    position: absolute;
    left: 212px; top: 40px;
    width: 1.5px; height: 170px;
    background: var(--brand-blue);
  }
  .details { position: absolute; left: 232px; top: 34px; right: 20px; }
  .person-name {
    color: var(--brand-blue);
    font-weight: 700;
    font-size: 24px;
    margin-bottom: 6px;
  }
  .credentials { font-size: 13px; line-height: 1.45; margin-bottom: 10px; }
  .contact-list { list-style: none; font-size: 12.5px; }
  .contact-list li { display: flex; align-items: center; gap: 10px; line-height: 1.8; }
  .contact-list svg { width: 14px; height: 14px; flex: none; fill: var(--brand-blue); }
  .address-band {
    position: absolute;
    left: 0; right: 0; bottom: 30px;
    height: 46px;
    background: var(--brand-blue);
    color: var(--card-white);
    display: flex; align-items: center; justify-content: center; gap: 10px;
    font-size: 15px;
  }
  .address-band svg { width: 16px; height: 18px; fill: var(--card-white); }
</style>
</head>
<body>

<section class="card card-back" aria-label="Card back">
  <div class="back-mark">
    <p class="mark-name">Brookfarrow Osteopathy &amp; Dry Needling</p>
  </div>
  <div class="appointment">
    <div class="appointment-field"><span>Appointment Time</span><i></i></div>
    <div class="appointment-field"><span>Date</span><i></i></div>
  </div>
</section>

<section class="card card-front" aria-label="Card front">
  <div class="front-mark">
    <p class="mark-name">Brookfarrow Osteopathy &amp; Dry Needling</p>
  </div>
  <div class="divider"></div>
  <div class="details">
    <h1 class="person-name">Dr. Martin Pellowe</h1>
    <p class="credentials">Osteopath (B.Clin.Sci (Ost)<br>M.Ost BSC ECON (Hons)</p>
    <ul class="contact-list">
      <li>
        <svg viewBox="0 0 24 24" aria-hidden="true"><path d="M6.6 10.8a15.1 15.1 0 0 0 6.6 6.6l2.2-2.2a1 1 0 0 1 1-.25 11.4 11.4 0 0 0 3.6.57 1 1 0 0 1 1 1V20a1 1 0 0 1-1 1A17 17 0 0 1 3 4a1 1 0 0 1 1-1h3.5a1 1 0 0 1 1 1 11.4 11.4 0 0 0 .57 3.6 1 1 0 0 1-.25 1z"/></svg>
        000-555 010 234
      </li>
      <li>
        <svg viewBox="0 0 24 24" aria-hidden="true"><path d="M2 5h20v14H2z" fill="none"/><path d="M2 5h20v2l-10 6L2 7zM2 9l10 6 10-6v10H2z"/></svg>
        info@brookfarrow.example
      </li>
      <li>
        <svg viewBox="0 0 24 24" aria-hidden="true"><path d="M12 2a10 10 0 1 0 0 20 10 10 0 0 0 0-20zm6.9 6h-3a15.6 15.6 0 0 0-1.4-3.6A8 8 0 0 1 18.9 8zM12 4a14 14 0 0 1 1.9 4h-3.8A14 14 0 0 1 12 4zM4.3 14a8 8 0 0 1 0-4h3.4a16.5 16.5 0 0 0 0 4zm.8 2h3a15.6 15.6 0 0 0 1.4 3.6A8 8 0 0 1 5.1 16zm3-8h-3a8 8 0 0 1 4.3-3.6A15.6 15.6 0 0 0 8.1 8zM12 20a14 14 0 0 1-1.9-4h3.8A14 14 0 0 1 12 20zm2.3-6H9.7a14.7 14.7 0 0 1 0-4h4.6a14.7 14.7 0 0 1 0 4zm.3 5.6a15.6 15.6 0 0 0 1.4-3.6h3a8 8 0 0 1-4.4 3.6zm1.7-5.6a16.5 16.5 0 0 0 0-4h3.4a8 8 0 0 1 0 4z"/></svg>
        www.brookfarrowosteosteopathy.example
      </li>
    </ul>
  </div>
  <div class="address-band">
    <svg viewBox="0 0 24 28" aria-hidden="true"><path d="M12 0a10 10 0 0 0-10 10c0 7.5 10 18 10 18s10-10.5 10-18A10 10 0 0 0 12 0zm0 14a4 4 0 1 1 0-8 4 4 0 0 1 0 8z"/></svg>
    48 Lower Crane Street Brookfarrow
  </div>
</section>

</body>
</html>
```